Business Card and Letterhead for Juniper Anvil - (Have Logo)

Update 4: Removed company reg no from business card details as it looked a bit out of place. Updated services list.
UPDATE 3
Sorry, I got the address a little bit wrong, have updated it below. Sorry for any inconvenience caused.
UPDATE 2
Finally I have the details for the business cards and letterhead. Submissions already made do not have to be updated unless shortlisted, if all new submissions could include the details for me, Marcus, that would be very much appreciated and help with the final shortlist selection. I intend to share a shortlist of the three best entries with past and existing customers for their feedback and opinions. Thank you all again for your time.
Here are the details.
Marcus Telby
Web Developer
T: 01632 960 418
E: marcus@juniperanvil.example
www.juniperanvil.example
Professional Photography
Web Solutions & E-Commerce
Audio & HD Video Production
Marketing & Promotions
Identity and Branding
Juniper Anvil Ltd
Suite 20938, 3rd Floor
212-224 Orchard Lane
London, N7 9QX
Company Reg. No: 05829147
The order and the layout of the information are of course down to the design, but the company registration number should be smaller and less prominent. The formatting of the telephone and email address using a T: and an E: I am not sure about and again if it is Tel: or Email: or Icons is up to the design.
The Company No. on the letterhead should read (somewhere in small text along the bottom):
Juniper Anvil is a Ltd Company registered in England & Wales, Registration No. 05829147.
The second business card details are
Oliver Brackley
Photographer
T: 01632 960 418
E: oliver@juniperanvil.example
Everything else the same of course.
Thank you again for all the submissions so far.
END OF UPDATE 2
-
UPDATE 1: Please do not alter the logo nor the logo colours. (This was a previous pixel forum project and I am extremely happy with it. The icon can stand alone of course, but I have had to eliminate all entries that have made it black and white, or reversed the icon.) I would like to thank everyone that has participated so far and am very grateful for all your thought and time.
End of Update 1
-
Original Brief:
I have attached the logo vector file.
Following a superb logo from a previous Pixel Forum project I am now looking for a business card design and (although less important) a letterhead as well.
I must admit I tried to do it myself but could only come up with the usual amateur stuff that in comparison to the quality of the logo looked awful.
About Us
Juniper Anvil Ltd will be a new company due to start in January. It is really just me (a web developer) and my friend (a photographer). We will be aiming at the usual small to medium sized businesses in the local area, selling various digital services including photographic services to the public, web hosting and development, commercial photography, modelling services (not us!), full video and film production and possibly a bit of marketing as well. (Really it is anything we can do professionally all lumped together! We met running seperate businesses which have both since closed)
We will not be competing on price. We plan to be expensive but fair. Certainly not the cheapest.
What we are looking for
Business Card
I imagine a double sided business card, which will be used for more than one person. I imagine the front to be the same for everyone and the persons details to be on the back, although this is of course only my thoughts and I am of course completely open to any ideas.
The card could also have a services list or a bit about what we do on it. It might feature the website address, our business address (mail forwarding address) or our registered company number.
Or it might have none of that, we are completely open to any ideas and have no real fixed opinions. I just want it to be really nice :-)
Letterhead (secondary importance)
We will make our decision primarily on the business card, although a mathcing letterhead would be fantastic. Something standardish in format and simple, although again, all ideas are welcomed.
I hope that is enough information but if you have any questions I will answer them as fully and as quickly as possible.
Thank you once again and I really look forward to seeing your ideas and picking a winner.
Marcus T.
Small businesses AND the general public
Film Production

```html
<!DOCTYPE html>
<html lang="en">
<head>
<meta charset="utf-8">
<title>Juniper Anvil – Business Card and Letterhead</title>
<link rel="stylesheet" href="https://fonts.googleapis.com/css2?family=Arimo:wght@400;700&display=swap">
<style>
  :root {
    --ink: #1f1f1f;
    --band: #232323;
    --paper: #ffffff;
    --brand-red: #c4161c;
    --muted: #444444;
    --shadow: rgba(0, 0, 0, 0.45);
  }
  * { box-sizing: border-box; margin: 0; padding: 0; }
  html, body {
    width: 1190px;
    height: 1200px;
    overflow: hidden;
    background: var(--paper);
    font-family: "Arimo", Arial, sans-serif;
    color: var(--ink);
  }
  .sheet { position: relative; width: 1190px; height: 1200px; }

  .side-label {
    position: absolute;
    top: 4px;
    font-size: 19px;
    color: var(--ink);
    letter-spacing: 0.5px;
  }
  .side-label--front { left: 10px; }
  .side-label--reverse { left: 633px; }

  .card {
    position: absolute;
    width: 536px;
    height: 297px;
    overflow: hidden;
    box-shadow: 6px 6px 8px var(--shadow);
  }

  /* Front of card */
  .card--front {
    left: 62px;
    top: 37px;
    background: var(--paper);
    border: 1px solid #bdbdbd;
  }
  .card__holder {
    position: absolute;
    right: 54px;
    top: 62px;
    text-align: right;
  }
  .card__name { font-weight: 700; font-size: 21px; }
  .card__role { font-size: 19px; margin-top: 5px; }

  .brand {
    position: absolute;
    display: flex;
    align-items: center;
    gap: 14px;
    font-weight: 700;
    color: var(--ink);
    letter-spacing: 1px;
    white-space: nowrap;
  }
  .brand__square { background: var(--brand-red); flex: none; }
  .card--front .brand { left: 40px; top: 180px; font-size: 42px; }
  .card--front .brand__square { width: 34px; height: 34px; }

  .card__footer {
    position: absolute;
    left: 0; right: 0; bottom: 0;
    height: 44px;
    background: var(--band);
    color: var(--paper);
    font-size: 18px;
    display: flex;
    align-items: center;
    justify-content: flex-end;
    padding-right: 26px;
  }

  /* Reverse of card */
  .card--reverse {
    left: 631px;
    top: 37px;
    background: var(--band);
    color: var(--paper);
  }
  .services__title { position: absolute; left: 51px; top: 50px; font-size: 16px; }
  .services__list {
    position: absolute;
    top: 92px;
    list-style: none;
    font-size: 12.5px;
    line-height: 16px;
  }
  .services__list li::before { content: "* "; }
  .services__list--left { left: 51px; }
  .services__list--right { left: 311px; top: 98px; }

  .card__contact-strip {
    position: absolute;
    left: 0; right: 0;
    top: 222px;
    height: 34px;
    background: var(--paper);
    color: var(--ink);
    font-size: 17px;
    display: flex;
    align-items: center;
  }
  .card__address { margin-left: 51px; }
  .card__phone { margin-left: 100px; }
  .card__email {
    position: absolute;
    left: 0; right: 0;
    bottom: 8px;
    text-align: center;
    font-size: 17px;
  }

  /* Letterhead */
  .letterhead {
    position: absolute;
    left: 10px;
    top: 367px;
    width: 612px;
    height: 822px;
    background: var(--paper);
    border: 1px solid #9a9a9a;
    box-shadow: 7px 7px 9px var(--shadow);
    overflow: hidden;
  }
  .letterhead .brand { left: 22px; top: 718px; font-size: 32px; }
  .letterhead .brand__square { width: 26px; height: 26px; }
  .letterhead__web {
    position: absolute;
    left: 342px;
    top: 752px;
    font-size: 16px;
  }
  .letterhead__footer {
    position: absolute;
    left: 0; right: 0; bottom: 0;
    height: 36px;
    background: var(--band);
    color: var(--paper);
    font-size: 16px;
    display: flex;
    align-items: center;
  }
  .letterhead__address { margin-left: 58px; }
  .letterhead__phone { margin-left: 120px; }
</style>
</head>
<body>
<main class="sheet">
  <span class="side-label side-label--front">FRONT</span>
  <span class="side-label side-label--reverse">REVERSE</span>

  <section class="card card--front" aria-label="Business card front">
    <div class="card__holder">
      <p class="card__name">Mr. Marcus Telby</p>
      <p class="card__role">Production Manager</p>
    </div>
    <div class="brand">
      <span class="brand__square"></span>
      <span class="brand__name">JUNIPER ANVIL</span>
    </div>
    <div class="card__footer">www.juniperanvil.example</div>
  </section>

  <section class="card card--reverse" aria-label="Business card reverse">
    <p class="services__title">Services:</p>
    <ul class="services__list services__list--left">
      <li>Photography</li>
      <li>Web Development</li>
      <li>HD Video Production</li>
      <li>Marketing</li>
      <li>Branding</li>
    </ul>
    <ul class="services__list services__list--right">
      <li>Web Hosting</li>
      <li>E-Commerce</li>
      <li>Audio Production &amp; Editing</li>
      <li>Promotions</li>
      <li>Identity</li>
    </ul>
    <div class="card__contact-strip">
      <span class="card__address">Birch row 118-C, NY</span>
      <span class="card__phone">(01)555 472 19 63</span>
    </div>
    <p class="card__email">juniper-marcus@mailhaven.example</p>
  </section>

  <section class="letterhead" aria-label="Letterhead">
    <div class="brand">
      <span class="brand__square"></span>
      <span class="brand__name">JUNIPER ANVIL</span>
    </div>
    <p class="letterhead__web">www.juniperanvil.example</p>
    <div class="letterhead__footer">
      <span class="letterhead__address">Birch row 118-C, NY</span>
      <span class="letterhead__phone">(01)555 472 19 63</span>
    </div>
  </section>
</main>
</body>
</html>
```